Redesign Login page

I want to redesign my login page to bring my 2 products closer together. I am only looking to redesign one login page, not 2.

For the logo, please make it solid and it can be black or white if helpful. I can also fine tune the logo if you get it close.

Coding

Coded - Design and coding required

Number of Pages Required

1 page

```html
<!DOCTYPE html>
<html lang="en">
<head>
<meta charset="utf-8">
<title>Trelvo – Login</title>
<link href="https://fonts.googleapis.com/css2?family=Roboto:wght@400;500;700&display=swap" rel="stylesheet">
<style>
  :root {
    --page-bg: #ffffff;
    --card-bg: #ffffff;
    --brand-green: #43655f;
    --brand-dark: #1f2a28;
    --logo-grey: #5a5a5a;
    --text-muted: #6b6b6b;
    --text-label: #5f5f5f;
    --field-border: #c9c9c9;
    --checkbox-border: #d8d8d8;
  }
  * { margin: 0; padding: 0; box-sizing: border-box; }
  html, body {
    width: 1030px; height: 1200px; overflow: hidden;
    background: var(--page-bg);
    font-family: "Roboto", Arial, sans-serif;
  }
  .login-card {
    position: absolute; left: 122px; top: 96px;
    width: 774px; height: 904px;
    background: var(--card-bg);
    border-radius: 40px;
    box-shadow: 0 6px 40px rgba(0,0,0,0.07);
  }
  .brand-name {
    position: absolute; left: 0; right: 0; top: 78px;
    text-align: center;
    font-size: 62px; font-weight: 700; letter-spacing: -1px;
    color: var(--logo-grey); line-height: 1;
  }
  .welcome-text {
    position: absolute; left: 0; right: 0; top: 178px;
    text-align: center; font-size: 18px; color: var(--text-muted);
  }
  .form-area { position: absolute; left: 110px; top: 250px; width: 554px; }
  .text-field {
    position: absolute; left: 0; width: 554px; height: 74px;
    border: 1px solid var(--field-border);
    padding: 12px 0 0 26px;
  }
  .text-field.is-focused { border-left: 3px solid var(--brand-dark); padding-left: 24px; }
  .field-email { top: 0; }
  .field-password { top: 93px; }
  .field-label { display: block; font-size: 18px; color: var(--text-label); line-height: 22px; }
  .field-value { display: block; font-size: 18px; color: var(--brand-green); line-height: 30px; font-weight: 500; }
  .field-password .field-value { letter-spacing: 0.5px; font-size: 16px; }
  .options-row {
    position: absolute; left: 0; top: 187px; width: 554px;
    display: flex; justify-content: space-between; align-items: center;
    font-size: 18px; color: var(--text-label);
  }
  .remember { display: flex; align-items: center; gap: 14px; }
  .checkbox { width: 13px; height: 13px; border: 1px solid var(--checkbox-border); }
  .btn {
    position: absolute; left: 0; width: 554px; height: 54px;
    display: flex; align-items: center; justify-content: center;
    font-size: 18px; font-family: inherit;
  }
  .btn-login {
    top: 267px; background: var(--brand-green); color: #fff; border: none;
    box-shadow: 0 3px 4px rgba(0,0,0,0.2);
  }
  .divider-or {
    position: absolute; left: 0; width: 554px; top: 350px;
    text-align: center; font-size: 18px; color: var(--text-muted);
  }
  .btn-signup {
    top: 404px; background: #fff; color: var(--brand-dark);
    border: 1px solid var(--brand-green);
  }
  .social-row {
    position: absolute; left: 0; top: 514px; width: 554px;
    display: flex; justify-content: space-between; align-items: center;
    font-size: 18px;
  }
  .social-intro { color: var(--text-muted); width: 150px; }
  .social-link { color: var(--brand-green); font-weight: 700; text-decoration: none; }
</style>
</head>
<body>
  <main class="login-card">
    <div class="brand-name">Trelvo</div>
    <p class="welcome-text">Welcome&nbsp; back! Please login to your account.</p>

    <form class="form-area">
      <div class="text-field field-email is-focused">
        <span class="field-label">Email Address</span>
        <span class="field-value">user@trelvo.com</span>
      </div>
      <div class="text-field field-password">
        <span class="field-label">Password</span>
        <span class="field-value">*******************</span>
      </div>
      <div class="options-row">
        <label class="remember"><span class="checkbox"></span>Remember Me</label>
        <span class="forgot-link">Forgot Password?</span>
      </div>
      <button type="button" class="btn btn-login">Login</button>
      <div class="divider-or">OR</div>
      <button type="button" class="btn btn-signup">Sign Up</button>
      <div class="social-row">
        <span class="social-intro">Or login with</span>
        <a class="social-link">Chatterly</a>
        <a class="social-link">Workline</a>
        <a class="social-link">Searchly</a>
      </div>
    </form>
  </main>
</body>
</html>
```